Business Card Design for Venture Lantern

Venture Lantern is a pro bono student consultancy service offered by Solvari KPTC to social start ups and enterprises. We provide consulting services with expertise in areas such as Marketing, IT, Business Strategy and Innovation.
I have attached\ the Venture Lantern Logo here for your perusal.
Industry/Entity Type
Business
Contact Information for Business Card
Name: Dae Hwan Park Name: Thomas Leung
Role: Project Leader Role: Vice Project Leader
M:0491203846 M: 0473560218
E: dae-hwan.park@solvarikptc.org E: thomas.leung@solvarikptc.org
W: www.solvarikptc.org W: www.solvarikptc.org

```html
<!DOCTYPE html>
<html lang="en">
<head>
<meta charset="utf-8">
<title>Venture Lantern – Business Card</title>
<link rel="stylesheet" href="https://fonts.googleapis.com/css2?family=Arimo:wght@400;700&display=swap">
<style>
  :root {
    --card-dark: #2b2627;
    --card-light: #ffffff;
    --accent-orange: #e8902a;
    --text-light: #ffffff;
  }
  html, body {
    margin: 0;
    padding: 0;
    overflow: hidden;
    background: var(--card-light);
  }
  .card {
    position: relative;
    width: 1200px;
    height: 686px;
    background: var(--card-dark);
    overflow: hidden;
    font-family: "Arimo", Arial, sans-serif;
  }
  .card__curve {
    position: absolute;
    inset: 0;
    width: 1200px;
    height: 686px;
  }
  .card__curve path { fill: var(--card-light); }

  .brand-name {
    position: absolute;
    left: 64px;
    top: 238px;
    width: 460px;
    margin: 0;
    text-align: center;
    font-weight: 700;
    font-size: 64px;
    line-height: 1.05;
    color: var(--card-dark);
    letter-spacing: -1px;
  }

  .person {
    position: absolute;
    right: 55px;
    top: 30px;
    text-align: right;
    color: var(--text-light);
  }
  .person__name {
    margin: 0;
    font-weight: 400;
    font-size: 46px;
    line-height: 58px;
    padding: 0 0 4px 20px;
    border-bottom: 4px solid var(--accent-orange);
  }
  .person__role {
    margin: 12px 0 0;
    font-size: 25px;
  }

  .contact {
    position: absolute;
    right: 53px;
    top: 372px;
    margin: 0;
    text-align: right;
    color: var(--text-light);
    font-style: normal;
  }
  .contact__line { margin: 0; }
  .contact__line--mobile { font-size: 30px; line-height: 40px; }
  .contact__line--email { font-size: 27px; line-height: 40px; margin-top: 4px; }

  .website {
    position: absolute;
    right: 52px;
    bottom: 26px;
    margin: 0;
    font-size: 50px;
    color: var(--accent-orange);
  }
</style>
</head>
<body>
  <main class="card">
    <svg class="card__curve" viewBox="0 0 1200 686" aria-hidden="true">
      <path d="M0 0 H411 Q743 343 411 686 H0 Z"/>
    </svg>

    <h1 class="brand-name">Venture<br>Lantern</h1>

    <header class="person">
      <h2 class="person__name">Dae Hwan Park</h2>
      <p class="person__role">Project Leader</p>
    </header>

    <address class="contact">
      <p class="contact__line contact__line--mobile">Mobile : 0491203846</p>
      <p class="contact__line contact__line--email">E-mail : dae-hwan.park@solvarikptc.org</p>
    </address>

    <p class="website">www.solvarikptc.org</p>
  </main>
</body>
</html>
```